Circus Poster 2016

We want to revise our circus poster for our 2016 tour. We very much liked the poster we used last year (attached) and want to stay with this colour scheme and with this logo. However, we want to enhance the family friendliness of the poster, so perhaps the addition of a family having a great time would be a good idea.

The winner will be paid to modify this poster for each of the 30 events we are doing this year plus making a flyer (based on the poster design). So the winner of this contest gets a job for a year.

```html
<!DOCTYPE html>
<html lang="en">
<head>
<meta charset="utf-8">
<title>Marlow's Circus 2016 Poster</title>
<link rel="stylesheet" href="https://fonts.googleapis.com/css2?family=Mulish:wght@400;600;800;900&display=swap">
<style>
  :root {
    --page: #fdf8e6;
    --night: #0d0d0d;
    --teal-deep: #0f4a4a;
    --teal: #1a8c8a;
    --teal-glow: #39c2b7;
    --logo-red: #e8363b;
    --brown-edge: #6a3a14;
    --sun-yellow: #f7d51c;
    --sun-orange: #ef8a1d;
    --sun-red: #d8322a;
    --label-yellow: #ffe600;
    --label-teal: #0fc1b2;
    --label-red: #e2372a;
    --label-black: #0a0a0a;
    --ink: #111111;
    --white: #ffffff;
    --free-cyan: #5fe3ff;
    --dot: #d9dde0;
  }
  * { margin: 0; padding: 0; box-sizing: border-box; }
  html, body { width: 1000px; height: 1200px; overflow: hidden; }
  body {
    background: var(--page);
    font-family: "Mulish", "Avenir Next", sans-serif;
    position: relative;
  }
  .poster {
    position: absolute;
    left: 130px; top: 75px;
    width: 748px; height: 1050px;
    background: var(--night);
    overflow: hidden;
  }
  .hero-photo {
    position: absolute; left: 0; top: 0; width: 748px; height: 380px;
    background:
      radial-gradient(ellipse 60% 30% at 55% 12%, rgba(214,170,70,.85), rgba(214,170,70,0) 70%),
      radial-gradient(ellipse 70% 40% at 35% 35%, rgba(230,60,40,.9), rgba(230,60,40,0) 75%),
      radial-gradient(ellipse 50% 45% at 85% 55%, rgba(240,110,40,.8), rgba(240,110,40,0) 75%),
      linear-gradient(180deg, #1a1208 0%, #8a3a1c 45%, #e9cbb4 100%);
  }
  .sunburst {
    position: absolute; left: 0; top: 600px; width: 748px; height: 450px;
    background:
      radial-gradient(ellipse 95% 110% at 50% 0%, var(--sun-yellow) 0%, var(--sun-orange) 40%, var(--sun-red) 70%, #7a2414 100%);
  }
  .marquee-panel {
    position: absolute; left: 0; top: 300px; width: 748px; height: 440px;
  }
  .side-dots { position: absolute; top: 490px; width: 12px; }
  .side-dots span {
    display: block; width: 11px; height: 11px; border-radius: 50%;
    background: var(--dot); margin-bottom: 6px;
  }
  .side-dots.left { left: 42px; }
  .side-dots.right { left: 706px; }
  .brand {
    position: absolute; left: 0; width: 748px; top: 388px;
    text-align: center; color: var(--logo-red); font-weight: 900;
  }
  .brand-small { display: block; font-size: 50px; line-height: 60px; }
  .brand-large { display: block; font-size: 118px; line-height: 124px; letter-spacing: 4px; margin-top: 4px; }
  .offer {
    position: absolute; left: 0; width: 748px; top: 619px;
    text-align: center; color: var(--white);
    font-size: 14px; line-height: 17px; font-weight: 600;
  }
  .offer em { font-style: normal; color: var(--free-cyan); }
  .label {
    position: absolute; color: var(--ink); font-weight: 400;
    white-space: nowrap; line-height: 1;
  }
  .label.town { left: 0; top: 737px; width: 560px; height: 72px; background: var(--label-yellow); font-size: 52px; padding: 10px 0 0 34px; }
  .label.venue { left: 198px; top: 815px; width: 550px; height: 52px; background: var(--label-teal); font-size: 44px; padding: 4px 0 0 34px; }
  .label.street { left: 62px; top: 870px; width: 443px; height: 34px; background: var(--label-red); font-size: 30px; padding: 2px 0 0 22px; }
  .label.dates { left: 182px; top: 907px; width: 386px; height: 70px; background: var(--label-black); color: var(--label-yellow); font-size: 44px; padding: 13px 0 0 0; text-align: center; }
  .contact {
    position: absolute; left: 0; width: 748px; top: 1002px;
    text-align: center; color: var(--white);
    font-size: 21px; font-weight: 600; letter-spacing: 3px;
  }
</style>
</head>
<body>
  <main class="poster">
    <div class="hero-photo" role="img" aria-label="Photo of a smiling family of four with a waving clown in front of an illuminated circus marquee sign"></div>
    <div class="sunburst" role="img" aria-label="Yellow, orange and red sunburst ray background"></div>

    <svg class="marquee-panel" viewBox="0 0 748 440" aria-hidden="true">
      <defs>
        <radialGradient id="panelGlow" cx="50%" cy="50%" r="60%">
          <stop offset="0" stop-color="var(--teal-glow)"/>
          <stop offset=".55" stop-color="var(--teal)"/>
          <stop offset="1" stop-color="var(--teal-deep)"/>
        </radialGradient>
      </defs>
      <rect x="0" y="64" width="748" height="254" fill="var(--night)"/>
      <path d="M0 310 H18 Q78 312 108 322 Q248 354 328 366 Q360 372 374 426 Q388 372 420 366 Q500 354 640 322 Q670 312 730 310 H748 V330 Q680 330 646 340 Q504 372 424 382 Q392 388 374 436 Q356 388 324 382 Q244 372 102 340 Q68 330 0 330 Z" fill="var(--brown-edge)"/>
      <path d="M10 60 L318 62 Q340 62 350 42 Q362 18 374 16 Q386 18 398 42 Q408 62 430 62 L738 60 V68 H10 Z" fill="var(--night)"/>
      <path d="M18 64 L318 66 Q340 66 350 46 Q362 24 374 22 Q386 24 398 46 Q408 66 430 66 L730 64 V315 Q670 318 640 328 Q500 360 420 372 Q388 378 374 415 Q360 378 328 372 Q248 360 108 328 Q78 318 18 315 Z" fill="url(#panelGlow)"/>
      <circle cx="374" cy="64" r="5" fill="var(--white)" opacity=".9"/>
      <circle cx="360" cy="372" r="7" fill="var(--dot)" opacity=".7"/>
    </svg>

    <div class="side-dots left"><span></span><span></span><span></span><span></span></div>
    <div class="side-dots right"><span></span><span></span><span></span><span></span></div>

    <h1 class="brand">
      <span class="brand-small">Marlow's</span>
      <span class="brand-large">CIRCUS</span>
    </h1>
    <p class="offer">One <em>FREE KIDS TICKET</em> with every full-priced Adult ticket<br>purchased online or via phone/</p>

    <p class="label town">WESTHAMPTON</p>
    <p class="label venue">ASHGROVE PARK</p>
    <p class="label street">HARBOUR RD. BN17 4QX</p>
    <p class="label dates">25-31 MAY 2016</p>

    <p class="contact">MARLOWSCIRCUS.COM • 01632 555 718</p>
  </main>
</body>
</html>
```